Vorminta - Plastic to Diesel Energy Needs A Website

Make website explaining the concept and the team behind the company
Updates

I will be providing A logo and Information about the company upon signed NDA.

Coding

Coded - Design and coding required

Number of Pages Required

5+ page

```html
<!DOCTYPE html>
<html lang="en">
<head>
<meta charset="utf-8">
<title>Vorminta – Plastic to Diesel Energy</title>
<link href="https://fonts.googleapis.com/css2?family=Audiowide&family=Montserrat:wght@400;500;600;700&display=swap" rel="stylesheet">
<style>
:root{
  --blue:#1b6fc0;
  --blue-deep:#1563b3;
  --green:#8dc63f;
  --green-dark:#3f5f0a;
  --ink:#2b2b2b;
  --muted:#555;
  --white:#fff;
  --team-bg:#deeefc;
}
*{box-sizing:border-box;margin:0;padding:0}
html,body{width:1200px;height:3574px;overflow:hidden}
body{font-family:'Montserrat',sans-serif;color:var(--ink);background:#fff;position:relative}
.display{font-family:'Audiowide',sans-serif;text-transform:uppercase;letter-spacing:1px}
.btn{display:inline-flex;align-items:center;justify-content:center;border-radius:24px;color:#fff;font-weight:700;font-size:14px;text-decoration:none}
.btn-green{background:var(--green)}
.btn-blue{background:var(--blue)}
.mark{display:block;width:18px;height:18px;border-radius:50%;background:var(--green);margin:0 auto 8px}

/* header */
.site-header{position:absolute;top:0;left:0;width:1200px;height:84px}
.brand{position:absolute;left:111px;top:20px}
.brand-name{display:flex;align-items:center;gap:8px;font-weight:700;font-size:30px;color:var(--blue);line-height:1}
.brand-name i{width:12px;height:12px;border-radius:50%;background:var(--green)}
.brand-tag{font-size:10px;color:var(--green);font-weight:600;margin-top:4px;letter-spacing:.3px}
.nav{position:absolute;left:580px;top:30px;display:flex;gap:33px;font-size:14px}
.nav a{color:#444;text-decoration:none}
.nav a.active{color:#111;font-weight:600}
.header-cta{position:absolute;left:939px;top:17px;width:150px;height:44px}

/* hero */
.hero{position:absolute;top:84px;left:0;width:1200px;height:522px;background:linear-gradient(90deg,#1f6f7c 0%,#3aa0a8 35%,#8fb64a 55%,#f1c400 72%,#f7d300 100%)}
.hero-panel{position:absolute;left:114px;top:91px;width:972px;height:333px;background:rgba(52,82,4,.9);border-radius:6px;text-align:center;padding-top:58px}
.hero h1{color:#fff;font-size:28px;font-weight:400}
.hero h1 span{display:block;color:var(--green);font-size:40px;margin-top:2px}
.hero p{color:#fff;font-size:14px;line-height:24px;width:620px;margin:20px auto 0}
.hero p b{font-weight:600}
.hero-actions{margin-top:22px;display:flex;justify-content:center;gap:10px}
.hero-actions .btn{height:44px;padding:0 24px}

/* about */
.about{position:absolute;top:606px;left:0;width:1200px;height:595px}
.about .mark{margin:0 0 6px 132px}
.about-text{position:absolute;left:112px;top:100px;width:406px}
.about h2{font-size:40px;color:var(--blue);font-weight:400}
.about p{font-size:14px;line-height:24px;color:#333;text-align:justify;margin-top:14px}
.about p + p{margin-top:8px}
.about .btn{margin-top:28px;width:158px;height:45px}
.about-art{position:absolute;left:652px;top:66px;width:388px;height:476px;border-radius:45% 40% 50% 35%;background:radial-gradient(circle at 50% 55%,#5c9b3c 0%,#2f7a2c 45%,#1f68b4 80%,#8dc63f 100%)}

/* why */
.why{position:absolute;top:1201px;left:0;width:1200px;height:759px;background:linear-gradient(200deg,#73b76a 0%,#4c9d86 35%,#2378b4 70%,#1a66b8 100%);text-align:center}
.why .mark{background:#fff;margin-top:94px}
.why h2{color:#fff;font-size:42px;font-weight:400}
.why-grid{position:absolute;left:112px;top:239px;width:978px;display:grid;grid-template-columns:repeat(3,314px);gap:19px 18px}
.why-card{background:#fff;height:180px;display:flex;flex-direction:column;align-items:center;padding-top:30px;font-size:17px;font-weight:500;color:#333;line-height:22px}
.why-card svg{width:58px;height:58px;margin-bottom:20px}
.r-tr{border-radius:0 70px 0 0}.r-tl{border-radius:70px 0 0 0}
.r-bl{border-radius:0 0 0 70px}.r-br{border-radius:0 0 70px 0}

/* lifecycle */
.lifecycle{position:absolute;top:1960px;left:0;width:1200px;height:713px;text-align:center}
.lifecycle .mark{margin-top:96px}
.section-title{font-size:40px;color:var(--blue);font-weight:400}
.section-sub{font-size:14px;line-height:24px;color:#333;width:470px;margin:24px auto 0}
.product-row{position:absolute;left:111px;top:283px;display:flex;gap:21px}
.product{width:312px;height:323px;background:#fff;box-shadow:0 2px 8px rgba(0,0,0,.1);text-align:left;border-radius:4px;overflow:hidden}
.product-img{height:197px}
.product h3{font-size:17px;font-weight:700;color:#222;margin:36px 0 0 25px}
.product p{font-size:13px;color:#555;margin:8px 0 0 26px}

/* team */
.team{position:absolute;top:2673px;left:0;width:1200px;height:643px;background:var(--team-bg);text-align:center}
.team .mark{margin-top:84px}
.team-row{position:absolute;left:111px;top:252px;display:flex;gap:12px}
.member{width:186px;height:204px;border-radius:4px;position:relative;background:linear-gradient(160deg,#6f8aa6 0%,#2f4c6d 60%,#1e3350 100%)}
.member span{position:absolute;left:33px;top:152px;color:#fff;font-weight:700;font-size:16px}
.team .btn{position:absolute;left:520px;top:496px;width:158px;height:45px}

/* footer */
.site-footer{position:absolute;top:3316px;left:0;width:1200px;height:258px;background:linear-gradient(200deg,#6db866 0%,#3f94a0 45%,#1a66b8 100%);color:#fff}
.footer-brand{position:absolute;left:110px;top:80px}
.footer-brand .brand-name{color:#fff;font-size:38px}
.footer-brand .brand-name i{background:#fff}
.footer-brand .brand-tag{color:#fff;font-size:14px}
.footer-brand small{display:block;font-size:13px;margin-top:22px}
.footer-col{position:absolute;top:86px;font-size:14px;line-height:21px}
.footer-col h4{font-size:13px;font-weight:500;margin-bottom:14px}
.footer-col a{display:block;color:#fff;text-decoration:none}
</style>
</head>
<body>

<header class="site-header">
  <div class="brand">
    <div class="brand-name"><i></i>Vorminta</div>
    <div class="brand-tag">PLASTIC TO DIESEL ENERGY</div>
  </div>
  <nav class="nav">
    <a class="active" href="#">Home</a><a href="#">About Us</a><a href="#">Our Team</a><a href="#">Contact</a>
  </nav>
  <a class="btn btn-green header-cta" href="#">Partner With Us</a>
</header>

<section class="hero" role="img" aria-label="Crushed plastic bottles blending into golden diesel fuel with bubbles">
  <div class="hero-panel">
    <h1 class="display">Investing in a<span>Sustainable Future</span></h1>
    <p>Vorminta converts non-recyclable plastic into high-quality diesel fuel — <b>reducing landfill waste while powering commercial industries.</b></p>
    <div class="hero-actions">
      <a class="btn btn-blue" href="#">Learn How It Works</a>
      <a class="btn btn-green" href="#">Partner With Us</a>
    </div>
  </div>
</section>

<section class="about">
  <div class="about-text">
    <span class="mark"></span>
    <h2 class="display">About Us</h2>
    <p>Vorminta provides a solution by converting waste plastic into usable diesel fuel through advanced thermal conversion technology.</p>
    <p>An integrated plastic waste conversion entity in the US. Secured feedstock supply chains and confirmed offtake partners, ensuring consistent operation and reliable revenue.&nbsp; Dual benefit opportunity - powerful environmental impact combined with strong, repeatable profitability.</p>
    <a class="btn btn-green" href="#">Learn More</a>
  </div>
  <div class="about-art" role="img" aria-label="Recycling arrows filled with an aerial view of green forest and rivers"></div>
</section>

<section class="why">
  <span class="mark"></span>
  <h2 class="display">Why Vorminta</h2>
  <div class="why-grid">
    <div class="why-card r-tr">
      <svg viewBox="0 0 58 58" fill="none" stroke="#1b6fc0" stroke-width="2.5"><rect x="8" y="46" width="22" height="6"/><path d="M19 46V34l14-14 10 8"/><circle cx="19" cy="34" r="3"/><circle cx="33" cy="20" r="3"/><path d="M43 28l6-4M43 28l4 7"/></svg>
      24/7 High-Utilization<br>Revenue Engine
    </div>
    <div class="why-card r-tl">
      <svg viewBox="0 0 58 58" fill="none" stroke-width="2.5"><rect x="18" y="8" width="30" height="30" stroke="#1b6fc0"/><rect x="8" y="20" width="30" height="30" stroke="#8dc63f" fill="#fff"/></svg>
      Low CAPEX, Modular<br>Replication Model
    </div>
    <div class="why-card r-tl">
      <svg viewBox="0 0 58 58" fill="none" stroke="#1b6fc0" stroke-width="2.5"><circle cx="29" cy="29" r="22"/><ellipse cx="29" cy="29" rx="10" ry="22"/><path d="M7 29h44M11 18h36M11 40h36"/></svg>
      Global Reach with Local<br>Strength
    </div>
    <div class="why-card r-bl">
      <svg viewBox="0 0 58 58" fill="none" stroke="#1b6fc0" stroke-width="2.5"><circle cx="29" cy="31" r="14"/><path d="M29 6v8M29 48v6M6 31h7M45 31h7M13 15l5 5M40 42l5 5M45 15l-5 5M18 42l-5 5"/><path d="M29 38c-5-4-3-10 0-12 3 2 5 8 0 12z" stroke="#8dc63f"/></svg>
      Industry Experience
    </div>
    <div class="why-card r-br">
      <svg viewBox="0 0 58 58" fill="none" stroke="#8dc63f" stroke-width="2.5"><circle cx="29" cy="29" r="10"/><circle cx="29" cy="29" r="4"/><circle cx="9" cy="9" r="4"/><circle cx="49" cy="9" r="4"/><circle cx="9" cy="49" r="4"/><circle cx="49" cy="49" r="4"/><path d="M12 12l9 9M46 12l-9 9M12 46l9-9M46 46l-9-9"/></svg>
      Feedstock &amp; Offtake<br>De-Risked Upfront
    </div>
    <div class="why-card r-bl">
      <svg viewBox="0 0 58 58" fill="none" stroke="#1b6fc0" stroke-width="2.5"><circle cx="29" cy="29" r="22"/><circle cx="29" cy="29" r="15"/><path d="M29 38c-9-2-12-10-10-14 6 0 10 5 10 14zM29 38c9-2 12-10 10-14-6 0-10 5-10 14z" stroke="#8dc63f"/></svg>
      Sustainability Focus
    </div>
  </div>
</section>

<section class="lifecycle">
  <span class="mark"></span>
  <h2 class="display section-title">Product Lifecycle</h2>
  <p class="section-sub">Transforming plastic waste into valuable energy through advanced pyrolysis technology.</p>
  <div class="product-row">
    <article class="product">
      <div class="product-img" role="img" aria-label="Plastic pellets, foam sheets and film rolls" style="background:linear-gradient(135deg,#f1efe9 0%,#d9dde0 50%,#b9c7d2 100%)"></div>
      <h3>Plastic Feedstock</h3>
      <p>Flexible plastic used in bags and films</p>
    </article>
    <article class="product">
      <div class="product-img" role="img" aria-label="Pyrolysis reactor with heated chamber and piping" style="background:linear-gradient(180deg,#8fb4d6 0%,#5b7ea3 55%,#e0823a 75%,#3a5a8a 100%)"></div>
      <h3>Conversion Process</h3>
      <p>Advanced Pyrolysis Conversion</p>
    </article>
    <article class="product">
      <div class="product-img" role="img" aria-label="Steel processing equipment beside a glass of amber oil" style="background:linear-gradient(90deg,#3b3f45 0%,#8a9096 45%,#d9a520 65%,#6a6e72 100%)"></div>
      <h3>Output Product Segment</h3>
      <p>Pyrolysis Oil, Syngas, Carbon Black</p>
    </article>
  </div>
</section>

<section class="team">
  <span class="mark"></span>
  <h2 class="display section-title">Our Team</h2>
  <p class="section-sub">Transforming plastic waste into valuable energy through advanced pyrolysis technology.</p>
  <div class="team-row">
    <div class="member" role="img" aria-label="Portrait of team member Carvel in a suit"><span>Carvel</span></div>
    <div class="member" role="img" aria-label="Portrait of team member Dunmore in a suit"><span>Dunmore</span></div>
    <div class="member" role="img" aria-label="Portrait of team member R T in a suit"><span>R T</span></div>
    <div class="member" role="img" aria-label="Portrait of team member K L in a suit"><span>K L</span></div>
    <div class="member" role="img" aria-label="Portrait of team member P N in a suit"><span>P N</span></div>
  </div>
  <a class="btn btn-green" href="#">View All</a>
</section>

<footer class="site-footer">
  <div class="footer-brand">
    <div class="brand-name"><i></i>Vorminta</div>
    <div class="brand-tag">PLASTIC TO DIESEL ENERGY</div>
    <small>2026 Vorminta. All Rights Reserved.</small>
  </div>
  <div class="footer-col" style="left:502px">
    <h4>QUICK LINKS</h4>
    <a href="#">Home</a><a href="#">About Us</a><a href="#">Our Team</a><a href="#">Contact</a>
  </div>
  <div class="footer-col" style="left:694px">
    <h4>OTHER LINKS</h4>
    <a href="#">Term &amp; Conditions</a><a href="#">Privacy Policy</a><a href="#">Sitemap</a><a href="#">FAQ</a>
  </div>
  <div class="footer-col" style="left:922px">
    <h4>CONTACT US</h4>
    <a href="#">Call: +1 555-014-2290</a><a href="#">Email: hello@vorminta.com</a>
  </div>
</footer>

</body>
</html>
```